Stationary pack for BrightVane

BrightVane is a recently establish Solar brokerage company based in Australia. We have a number of sales staff who provide advice and guidance to both residential and commercial customers regarding solar systems (solar hot water and solar panels.)

In addition to our brokerage services we are also developing software for the solar industry, which will be used to automate the solar system install process. This system will be used by other companies in the solar industry including installers, wholesalers and government departments.

We are after a stationary pack that consists of the following: Business cards, compliments slip and letter head.

The EPS, AI, PNG etc files for the logo are attached.

For the business card:
The name and logo of the company need to be clearly visible. On the back of the business cards, we would like the logo. I am happy for you to split the image part of the logo from the text if you think it would look better a different way.

I would like the business cards to be easily readable with the following information on the front:
Name
(Please leave room for titles for the future – eg Sales Advisor.)
Mobile
Office
Email
Address
ABN

Letter heads:
I would prefer the address to be at the top

Compliments slips:
Only need to be one sided

Target Market(s)

BrightVane provides services to both residential and commercial customers. Our customers will be environmentally conscious.

Industry/Entity Type

Residential

Requirements
Must have
• Business cards must have the logo on the back.

```html
<!DOCTYPE html>
<html lang="en">
<head>
<meta charset="utf-8">
<title>BrightVane Stationery Pack</title>
<link rel="stylesheet" href="https://fonts.googleapis.com/css2?family=Open+Sans:wght@300;400;700&display=swap">
<style>
  :root {
    --paper: #ffffff;
    --edge: #9a9a9a;
    --brand-green: #5aa52c;
    --deep-green: #3f8f2a;
    --leaf-green: #8cc63f;
    --sun-yellow: #f7e431;
    --sun-orange: #f6a81c;
    --ink-blue: #2c3e8c;
    --ink-grey: #5a5a5a;
    --rule: #2c3e8c;
  }
  * { box-sizing: border-box; margin: 0; padding: 0; }
  html, body {
    width: 1200px; height: 900px; overflow: hidden;
    background: var(--paper);
    font-family: "Open Sans", Arial, sans-serif;
  }
  .canvas { position: relative; width: 1200px; height: 900px; }

  /* brand lockup */
  .brand { display: flex; flex-direction: column; align-items: flex-start; gap: 4px; }
  .brand-dot { border-radius: 50%; background: var(--brand-green); }
  .brand-name { color: var(--brand-green); font-weight: 700; line-height: 1; letter-spacing: -0.5px; }

  /* letterhead */
  .letterhead {
    position: absolute; left: 96px; top: 0; width: 674px; height: 890px;
    background: var(--paper); border: 1px solid var(--edge); overflow: hidden;
  }
  .letterhead-header { position: absolute; left: 18px; top: 30px; display: flex; }
  .letterhead-header .brand-dot { width: 44px; height: 44px; margin-left: 22px; }
  .letterhead-header .brand-name { font-size: 26px; }
  .header-rule { width: 2px; height: 116px; background: var(--rule); margin: 0 10px 0 14px; }
  .sender { color: var(--ink-blue); padding-top: 2px; }
  .sender-name { font-size: 14px; font-weight: 400; }
  .sender-title { font-size: 10px; margin-bottom: 12px; }
  .sender-details { list-style: none; font-size: 8px; line-height: 11px; color: var(--ink-grey); }
  .letterhead-graphic { position: absolute; left: 0; bottom: 0; width: 674px; height: 300px; }

  /* business cards */
  .card { position: absolute; left: 770px; width: 390px; height: 172px; overflow: hidden; }
  .card-back {
    top: 30px;
    background: radial-gradient(ellipse at 50% 50%, var(--sun-yellow) 0%, #f9c72a 55%, var(--sun-orange) 100%);
    display: flex; align-items: center; justify-content: center;
  }
  .card-back .brand { align-items: center; }
  .card-back .brand-dot { width: 40px; height: 40px; }
  .card-back .brand-name { font-size: 24px; }
  .card-front {
    top: 226px;
    background: radial-gradient(ellipse at 40% 20%, #fbeb45 0%, #f9cb2c 60%, var(--sun-orange) 100%);
  }
  .card-graphic { position: absolute; right: 0; bottom: 0; width: 390px; height: 172px; }
  .card-front .sender { position: absolute; left: 14px; top: 10px; }
  .card-front .sender-name { font-size: 13px; }
  .card-front .sender-title { font-size: 9px; margin-bottom: 8px; }
  .card-front .sender-details { font-size: 7px; line-height: 10px; color: var(--ink-blue); }
  .card-front .brand { position: absolute; left: 14px; bottom: 10px; flex-direction: row; align-items: center; gap: 4px; }
  .card-front .brand-dot { width: 10px; height: 10px; }
  .card-front .brand-name { font-size: 11px; color: var(--deep-green); }

  /* compliments slip */
  .comp-slip {
    position: absolute; left: 580px; top: 436px; width: 600px; height: 244px;
    background: var(--paper); border: 1px solid var(--edge); overflow: hidden;
  }
  .comp-slip .brand { position: absolute; left: 16px; top: 16px; }
  .comp-slip .brand-dot { width: 40px; height: 40px; margin-left: 26px; }
  .comp-slip .brand-name { font-size: 26px; }
  .comp-graphic { position: absolute; left: 0; top: 0; width: 600px; height: 244px; }
</style>
</head>
<body>
<main class="canvas">

  <section class="letterhead" aria-label="Letterhead">
    <svg class="letterhead-graphic" viewBox="0 0 674 300" role="img" aria-label="Curved solar panel array graphic in green tones">
      <defs>
        <linearGradient id="lh-green" x1="0" y1="0" x2="1" y2="0.4">
          <stop offset="0" stop-color="#e7f2dc"/>
          <stop offset="0.45" stop-color="#9fcf5c"/>
          <stop offset="1" stop-color="#4f9a3a"/>
        </linearGradient>
      </defs>
      <path d="M0 300 C120 150 330 40 674 20 L674 300 Z" fill="url(#lh-green)"/>
    </svg>
    <header class="letterhead-header">
      <div class="brand">
        <span class="brand-dot"></span>
        <span class="brand-name">BrightVane</span>
      </div>
      <span class="header-rule"></span>
      <div class="sender">
        <p class="sender-name">Name</p>
        <p class="sender-title">Sales Advisor</p>
        <ul class="sender-details">
          <li>Mobile</li><li>Office</li><li>Email</li><li>Address</li><li>ABN</li>
        </ul>
      </div>
    </header>
  </section>

  <section class="card card-back" aria-label="Business card back">
    <div class="brand">
      <span class="brand-dot"></span>
      <span class="brand-name">BrightVane</span>
    </div>
  </section>

  <section class="card card-front" aria-label="Business card front">
    <svg class="card-graphic" viewBox="0 0 390 172" role="img" aria-label="Curved solar panel array graphic in green tones">
      <defs>
        <linearGradient id="bc-green" x1="0" y1="0" x2="1" y2="0.5">
          <stop offset="0" stop-color="#d9e85a"/>
          <stop offset="0.5" stop-color="#9ccc4a"/>
          <stop offset="1" stop-color="#4f9a3a"/>
        </linearGradient>
      </defs>
      <path d="M40 172 C110 90 230 40 390 30 L390 172 Z" fill="url(#bc-green)"/>
    </svg>
    <div class="sender">
      <p class="sender-name">Name</p>
      <p class="sender-title">Sales Advisor</p>
      <ul class="sender-details">
        <li>Mobile</li><li>Office</li><li>Email</li><li>Address</li><li>ABN</li>
      </ul>
    </div>
    <div class="brand">
      <span class="brand-dot"></span>
      <span class="brand-name">BrightVane</span>
    </div>
  </section>

  <section class="comp-slip" aria-label="Compliments slip">
    <svg class="comp-graphic" viewBox="0 0 600 244" role="img" aria-label="Faint curved solar panel array graphic in pale green">
      <defs>
        <linearGradient id="cs-green" x1="0" y1="0" x2="1" y2="0">
          <stop offset="0" stop-color="#f6faf1"/>
          <stop offset="1" stop-color="#dcecd0"/>
        </linearGradient>
      </defs>
      <path d="M120 244 C230 120 400 40 600 20 L600 244 Z" fill="url(#cs-green)"/>
    </svg>
    <div class="brand">
      <span class="brand-dot"></span>
      <span class="brand-name">BrightVane</span>
    </div>
  </section>

</main>
</body>
</html>
```